Professional Business Cards for Recruiting Company

We'd like professional 2-sided business cards that reflect a color scheme that matches our website, www.quillmerbay.com, and / or logo that is attached.

Slogan used is "We Know People", but needs to be editable because we change it up to "We Find Builders", "We Speak Geek", etc.

Must includes logo, slogan, first and last name, address, email, mobile number and website address.

Files attached for ideas.

Thanks!

Contact Information for Business Card

Logo, Company name, First name, Last name, addresss, email, phone, website address.

Font styles to use
Sans Serif

Colors
0054AA
0677BA
7BADD7
CADEEF
E8F1F8

Requirements
Nice to have
• I do like the following designs. 22962062 and 22962651. Couple ideas anyway.

```html
<!DOCTYPE html>
<html lang="en">
<head>
<meta charset="utf-8">
<title>Quillmerbay Business Cards</title>
<link rel="stylesheet" href="https://fonts.googleapis.com/css2?family=Montserrat:wght@300;400;500;600;700&display=swap">
<style>
  :root {
    --backdrop: #8f7152;
    --brand-blue: #1d4f8b;
    --paper: #ffffff;
    --ink-gray: #555a60;
    --mark-gray: #6f7378;
  }
  * { margin: 0; padding: 0; box-sizing: border-box; }
  html, body { width: 900px; height: 1200px; overflow: hidden; }
  body {
    background: var(--backdrop);
    font-family: "Montserrat", Arial, sans-serif;
    position: relative;
  }
  .card {
    position: absolute;
    left: 80px;
    width: 742px;
    height: 440px;
    border-radius: 40px;
    overflow: hidden;
    box-shadow: 0 6px 14px rgba(0,0,0,0.45);
  }
  .card-front { top: 132px; background: var(--paper); }
  .card-back { top: 638px; background: var(--brand-blue); }

  .brand { position: absolute; display: flex; align-items: center; }
  .brand-square { flex: none; }
  .brand-text { display: flex; flex-direction: column; }
  .brand-name {
    font-weight: 300;
    line-height: 1;
    white-space: nowrap;
    padding-bottom: 5px;
    border-bottom: 2px solid currentColor;
  }
  .brand-descriptor {
    font-weight: 600;
    white-space: nowrap;
    margin-top: 7px;
  }

  .card-front .brand { left: 96px; top: 78px; }
  .card-front .brand-square { width: 60px; height: 60px; margin-right: 84px; background: var(--brand-blue); }
  .card-front .brand-name { font-size: 47px; letter-spacing: 0.5px; color: var(--brand-blue); }
  .card-front .brand-descriptor { font-size: 14px; letter-spacing: 1.3px; color: var(--mark-gray); }

  .card-back .brand { left: 90px; top: 180px; }
  .card-back .brand-square { width: 70px; height: 70px; margin-right: 93px; background: var(--paper); }
  .card-back .brand-name { font-size: 56px; letter-spacing: 1px; color: var(--paper); }
  .card-back .brand-descriptor { font-size: 15.5px; letter-spacing: 1.6px; color: var(--paper); }

  .contact-band {
    position: absolute;
    left: 0; top: 217px;
    width: 100%; height: 142px;
    background: var(--brand-blue);
    color: var(--paper);
  }
  .person {
    position: absolute;
    right: 420px; top: 48px;
    text-align: right;
  }
  .person-name { font-size: 25px; font-weight: 700; line-height: 1.1; }
  .person-title { font-size: 15px; font-weight: 400; margin-top: 4px; }
  .band-divider {
    position: absolute;
    left: 352px; top: 46px;
    width: 2px; height: 60px;
    background: var(--paper);
  }
  .contact-list {
    position: absolute;
    left: 377px; top: 42px;
    list-style: none;
    font-size: 15.5px;
    line-height: 22px;
  }
  .contact-list li { display: flex; align-items: center; }
  .contact-list svg { width: 14px; height: 14px; margin-right: 14px; fill: var(--paper); }

  .address {
    position: absolute;
    left: 0; top: 378px; width: 100%;
    text-align: center;
    font-size: 15.5px;
    color: var(--ink-gray);
    padding-right: 36px;
  }
  .slogan {
    position: absolute;
    left: 0; top: 376px; width: 100%;
    text-align: center;
    color: var(--paper);
    font-size: 17px;
    font-weight: 400;
    letter-spacing: 7px;
  }
</style>
</head>
<body>
  <section class="card card-front">
    <div class="brand">
      <span class="brand-square"></span>
      <div class="brand-text">
        <div class="brand-name">QUILLMERBAY</div>
        <div class="brand-descriptor">SKILLED TALENT SEARCH AND PLACEMENT</div>
      </div>
    </div>

    <div class="contact-band">
      <div class="person">
        <div class="person-name">Dana Holvik</div>
        <div class="person-title">President</div>
      </div>
      <span class="band-divider"></span>
      <ul class="contact-list">
        <li>
          <svg viewBox="0 0 16 16" aria-hidden="true"><path d="M1 6c0-2 3-3.5 7-3.5S15 4 15 6v1.5h-3.5V6c-1-.6-6-.6-7 0v1.5H1zM4 8.5h8l1.5 5h-11z"/></svg>
          (555) 014-2286
        </li>
        <li>
          <svg viewBox="0 0 16 16" aria-hidden="true"><path d="M1 3.5h14v1L8 9 1 4.5zM1 6l7 4.5L15 6v6.5H1z"/></svg>
          support@quillmerbay.com
        </li>
        <li>
          <svg viewBox="0 0 16 16" aria-hidden="true"><circle cx="8" cy="8" r="7"/><path d="M4 5l3 1-1 3 3 1-1 3" stroke="#1d4f8b" stroke-width="1.5" fill="none"/></svg>
          www.quillmerbay.com
        </li>
      </ul>
    </div>

    <p class="address">2210 Larkfield Park Circle N, Brenmoor, North Dakota 58000</p>
  </section>

  <section class="card card-back">
    <div class="brand">
      <span class="brand-square"></span>
      <div class="brand-text">
        <div class="brand-name">QUILLMERBAY</div>
        <div class="brand-descriptor">SKILLED TALENT SEARCH AND PLACEMENT</div>
      </div>
    </div>
    <p class="slogan">WE FIND BUILDERS</p>
  </section>
</body>
</html>
```